Brivo Packworks Website using Wix Platform

Project Overview:
Brivo Packworks is a supply chain company specializing in packaging and manufacturing services for CPG (Consumer Packaged Goods) brands and nutritional/dietary supplement companies. The company offers end-to-end solutions including packaging design, production, co-packing, and private labeling. The goal of this project is to create a professional, user-friendly website that showcases your expertise, builds trust with potential clients, and generates leads for your services.

Objectives:
Establish Brand Authority: Position Brivo Packworks as a leader in the packaging and manufacturing industry for CPG and nutritional products.
Lead Generation: Encourage visitors to contact you for quotes, consultations, or further information.
Professional User Experience: Ensure the website is easy to navigate, visually appealing, and mobile-friendly.
SEO & Conversion Optimization: Optimize the site for search engines to attract organic traffic and improve conversion rates.
Primary Audience:
CPG Brands: Companies in industries like food and beverage, personal care, and household products looking for packaging and manufacturing services.
Nutritional/Dietary Supplement Brands: Companies in the health and wellness industry needing specialized packaging and manufacturing services for supplements, including compliance with regulatory standards (GMP).
Secondary Audience:
Potential partners looking to collaborate on co-packing or private labeling.
Key Features & Functionality:
Responsive Design:

The website must be fully responsive, ensuring optimal viewing across all devices (desktops, tablets, mobile).
User-Centric Navigation:

A clean, intuitive navigation system that allows users to quickly access key pages such as Home, Services, About Us, Case Studies, FAQ, and Contact.
Lead Generation Forms:

Prominent CTAs (Calls to Action) throughout the website encouraging users to “Request a Quote”, “Get in Touch”, or “Learn More” about your services.
Contact Form: Simple form allowing potential clients to submit inquiries about your services.
SEO Optimization:

The site should be optimized for relevant keywords (e.g., “co-packing services for CPG,” “nutritional supplement packaging,” “custom packaging solutions”), including meta descriptions, headers, and on-page content.
Content Management System (CMS):

An easy-to-use CMS (like WordPress or Webflow) for easy content updates. This will allow you to make changes to your services, case studies, and other sections without requiring a developer.
Analytics Integration:

Google Analytics or a similar tool for tracking site visitors and performance metrics to make data-driven decisions on site improvements.
Site Structure & Content:
1. Home Page:
Hero Section with tagline, images or video of your services in action, and a clear CTA (e.g., “Request a Quote”).
Value Proposition: Short and compelling introduction to Brivo Packworks’s core services and advantages.
Overview of Services: Highlight your key offerings (e.g., Packaging Design, Co-packing, Nutritional Supplement Packaging, Private Labeling).
Client Logos/Testimonials: Social proof to establish credibility.
CTA Buttons: Throughout the page to drive conversions (e.g., “Get a Free Consultation”).
2. About Us Page:
Company Overview: Explain your mission, values, and commitment to quality.
Team Overview (Optional): Introduce key team members to humanize your company and build trust.
Core Values and Differentiators: Showcase what makes Brivo Packworks unique—sustainability practices, regulatory compliance, and industry expertise.
3. Services Pages (Separate Pages for Each Service):
Packaging & Design: Custom packaging solutions, materials, and design services for CPG brands.
Manufacturing & Assembly: Your end-to-end production process, assembly capabilities, and how you support both small and large-scale runs.
Nutritional & Dietary Supplement Packaging: Focus on specialized packaging for supplements, regulatory compliance (GMP), and certifications.
Private Labeling: Services for clients who wish to brand their own products using your packaging.
Each service page will include detailed descriptions, benefits, process information, and CTAs like “Get Started” or “Request a Quote”.
4. Case Studies / Portfolio Page:
Success Stories: Showcase in-depth case studies of past projects, especially successful partnerships with CPG or supplement brands.
Before & After Images: Display the difference your services have made for clients, especially in terms of packaging quality or branding improvements.
Client Testimonials: Additional customer feedback to strengthen your brand reputation.
5. FAQ Page:
Address common questions related to lead times, regulatory compliance, order quantities, and specific details for different industries (e.g., dietary supplements).
The format will be accordion-style or dropdowns for easy scanning.
6. Contact Us Page:
Contact Form: With fields for name, email, company, and inquiry details.
Location Information: Physical address, phone number, and working hours.
Map Integration: If relevant, integrate Google Maps to show your office location.
Social Media Links: Link to your company’s LinkedIn, Instagram, or other relevant platforms.

Target Market(s)

Startup CPG Brands, Supplement Brands, Nutrition Brands

Industry/Entity Type

Flexible Packaging, Contract Manufacturing, Supplement & Food Manufacturing

Coding

Coded - Design and coding required

Number of Pages Required

5+ page

Requirements
Must have
• Use our colors.
Nice to have
• https://tornap482.sitebuildhost.example/brivopackworks - www.ninefoldlane.example - www.pelkasnacks.example - thebrightmill.example

```html
<!DOCTYPE html>
<html lang="en">
<head>
<meta charset="utf-8">
<title>Brivo Packworks</title>
<link href="https://fonts.googleapis.com/css2?family=Outfit:wght@500;600;700&family=Poppins:wght@400;500;600&display=swap" rel="stylesheet">
<style>
:root{
  --navy:#25243f;
  --blue:#1e90f5;
  --blue-line:#2f7fd6;
  --ice:#eef3fb;
  --mist:#e8e8eb;
  --white:#ffffff;
  --ink:#1f1e35;
}
*{box-sizing:border-box;margin:0;padding:0}
html,body{width:1200px;height:4320px;overflow:hidden}
body{position:relative;background:var(--white);font-family:"Poppins",sans-serif;color:var(--ink)}
.abs{position:absolute}
.heading{font-family:"Outfit",sans-serif;font-weight:600;color:var(--ink);letter-spacing:-0.5px}
.divider{position:absolute;height:12px}
.divider::before,.divider::after{content:"";position:absolute;top:5px;width:calc(50% - 10px);height:2px;background:var(--blue-line)}
.divider::before{left:0}.divider::after{right:0}
.divider i{position:absolute;left:50%;top:2px;width:7px;height:7px;margin-left:-3.5px;background:var(--blue);transform:rotate(45deg)}
.btn-outline{position:absolute;border:2px solid var(--navy);border-radius:22px;font-size:14px;display:flex;align-items:center;justify-content:center;color:var(--ink)}

.topbar{left:0;top:0;width:1200px;height:84px;background:var(--navy)}
.brand{font-weight:500;color:var(--white);font-size:20px;display:flex;align-items:center;gap:10px}
.brand b{width:12px;height:12px;background:var(--blue);display:inline-block}
.nav a{position:absolute;top:27px;color:var(--white);font-size:14px;text-decoration:none}
.nav .active{border-bottom:2px solid #3fb68b;padding-bottom:6px}
.nav .pill{top:22px;left:1046px;width:90px;height:30px;border:1.5px solid #3fb68b;border-radius:16px;display:flex;align-items:center;justify-content:center}

.hero-photo{left:603px;top:84px;width:597px;height:580px;background:linear-gradient(135deg,#3b3430 0%,#6a5a48 35%,#c9ad85 60%,#a88a62 100%)}
.hero-title{left:66px;top:205px;font-family:"Outfit",sans-serif;font-weight:700;font-size:86px;line-height:100px;letter-spacing:1px;color:var(--ink)}
.hero-text{left:68px;top:432px;width:450px;font-size:14px;line-height:21px;color:#333}

.card{position:absolute;top:877px;width:213px;height:212px;background:var(--white);box-shadow:0 2px 10px rgba(0,0,0,.16)}
.card .icon{position:absolute;left:14px;top:16px;width:185px;height:112px;background:var(--white);box-shadow:0 1px 6px rgba(0,0,0,.12);display:flex;align-items:center;justify-content:center}
.card .label{position:absolute;left:0;bottom:0;width:100%;height:62px;background:var(--blue);color:var(--white);font-size:16px;font-weight:500;display:flex;align-items:center;justify-content:center}
.line-ico{fill:none;stroke:#1c1c24;stroke-width:2.4;stroke-linecap:round;stroke-linejoin:round}

.about-band{left:0;top:1155px;width:1200px;height:498px;background:var(--ice)}
.about-photo{left:97px;top:1173px;width:448px;height:461px;border-radius:48% 52% 44% 56% / 50% 46% 54% 50%;background:radial-gradient(circle at 55% 50%,#c9a57a 0%,#8a7058 40%,#3a3f3c 75%,#9ba09e 100%)}
.about-text{left:625px;top:1364px;width:470px;font-size:13.5px;line-height:21.5px;text-align:justify;color:#333}

.svc{position:absolute;top:1840px;width:240px;text-align:center}
.svc .ring{margin:0 auto;width:158px;height:158px;border-radius:50%;background:var(--white);box-shadow:0 2px 10px rgba(0,0,0,.18);display:flex;align-items:center;justify-content:center}
.svc p{margin-top:22px;font-size:16px;font-weight:600;line-height:21px}
.blue-ico{fill:none;stroke:var(--blue);stroke-width:2.4;stroke-linecap:round;stroke-linejoin:round}

.testi-band{left:0;top:2125px;width:1200px;height:771px;background:var(--ice)}
.testi-frame{left:313px;top:2335px;width:588px;height:440px;border:3px solid var(--navy);border-radius:6px}
.testi-card{left:215px;top:2412px;width:782px;height:303px;background:var(--blue)}
.avatar{left:572px;top:2352px;width:102px;height:102px;border-radius:50%;background:var(--white);box-shadow:0 2px 8px rgba(0,0,0,.2)}
.avatar span{position:absolute;left:30px;top:14px;width:42px;height:42px;border-radius:50%;background:linear-gradient(#8c7d70,#3d3a38)}
.avatar em{position:absolute;left:0;top:66px;width:100%;text-align:center;font-style:normal;font-size:11px;font-weight:500}
.quote-text{left:360px;top:2470px;width:510px;text-align:center;color:var(--white);font-size:20px;line-height:33px}
.stars{left:360px;top:2622px;width:490px;text-align:center;color:var(--white);font-size:30px;letter-spacing:8px}
.qmark{width:54px;height:54px;border-radius:50%;background:var(--white);box-shadow:0 2px 6px rgba(0,0,0,.2);font-family:Georgia,serif;font-size:34px;font-weight:700;display:flex;align-items:center;justify-content:center;line-height:1;padding-top:14px}
.arrow{width:34px;height:34px;border-radius:50%;background:var(--white);display:flex;align-items:center;justify-content:center}

.cta-band{left:0;top:2896px;width:1200px;height:433px;background:linear-gradient(120deg,#d8e6e0 0%,#c3d9d1 50%,#dfe8e2 100%)}
.cta-title{left:0;top:2948px;width:1200px;text-align:center;font-family:"Outfit",sans-serif;font-weight:600;font-size:76px;line-height:84px;color:#111}
.cta-btn{left:382px;top:3171px;width:438px;height:64px;border-radius:34px;background:var(--navy);color:var(--white);font-size:27px;display:flex;align-items:center;justify-content:center}

.contact-band{left:0;top:3329px;width:1200px;height:536px;background:var(--mist)}
.contact-photo{left:96px;top:3377px;width:416px;height:416px;border-radius:50%;border:6px solid var(--navy);background:linear-gradient(160deg,#f4f2ee 0%,#d9d4cb 55%,#b08a62 80%,#8f7a65 100%)}
.field{position:absolute;height:48px;background:var(--white);border:1px solid #e0e0e4;font-size:12px;color:#b0b0b8;padding:17px 10px}
.send{left:540px;top:3784px;width:98px;height:28px;border-radius:14px;background:var(--navy);color:var(--white);font-size:15px;display:flex;align-items:center;justify-content:center}

.footer{left:0;top:3865px;width:1200px;height:455px;background:var(--navy)}
.foot-h{position:absolute;top:3928px;font-size:22px;font-weight:500;color:var(--white)}
.foot-h::after{content:"";position:absolute;left:0;top:36px;width:52px;height:2px;background:#cfd2e6}
.foot-links{left:337px;top:3998px;list-style:none}
.foot-links li{font-size:16px;font-weight:500;color:var(--white);height:32.5px;padding-left:20px;position:relative}
.foot-links li::before{content:"";position:absolute;left:0;top:9px;width:7px;height:7px;border-radius:50%;background:var(--white)}
.info{position:absolute;left:604px;font-size:16px;line-height:22px;color:var(--white)}
.info-ico{position:absolute;left:557px;width:36px;height:36px;border-radius:50%;background:var(--white);display:flex;align-items:center;justify-content:center}
.social{position:absolute;top:4077px;width:37px;height:37px;border-radius:50%;background:var(--white)}
.news-field{left:820px;top:4065px;width:303px;height:47px;border-radius:8px;background:var(--white);font-size:14px;color:#9a9aa6;padding:13px 18px}
.subscribe{left:821px;top:4133px;width:136px;height:35px;border-radius:18px;background:var(--white);color:var(--ink);font-size:15px;display:flex;align-items:center;justify-content:center}
.rule{left:69px;top:4244px;width:1064px;height:1px;background:#9a9ab0}
.copyright{left:0;top:4272px;width:1200px;text-align:center;font-size:14px;color:var(--white)}
</style>
</head>
<body>

<header class="abs topbar">
  <div class="abs brand" style="left:72px;top:27px"><b></b>Brivo Packworks</div>
  <nav class="nav">
    <a class="active" style="left:606px">Home</a>
    <a style="left:678px">Services</a>
    <a style="left:774px">About Us</a>
    <a style="left:870px">Case Studies</a>
    <a style="left:990px">FAQ</a>
    <a class="pill">Contact</a>
  </nav>
</header>

<section>
  <div class="abs hero-photo" role="img" aria-label="Kraft paper pouch with a white Brivo Packworks label on a dark table"></div>
  <h1 class="abs hero-title">PACKAGING<br>MAKE&nbsp; EASY</h1>
  <p class="abs hero-text">Lorem ipsum dolor sit amet, consectetur adipiscing elit, sed do eiusmod tempor incididunt ut labore et dolore magna aliqua. Quis ipsum suspendisse ultrices gravida. Risus commodo</p>
  <div class="btn-outline" style="left:69px;top:536px;width:147px;height:41px">Request a Quote</div>
</section>

<section>
  <h2 class="abs heading" style="left:0;top:718px;width:1172px;text-align:center;font-size:58px">Why Choose Us</h2>
  <div class="divider" style="left:490px;top:815px;width:220px"><i></i></div>

  <div class="card" style="left:92px"><div class="icon">
    <svg class="line-ico" width="90" height="90" viewBox="0 0 90 90" aria-hidden="true">
      <path d="M44 40a12 12 0 1 0-14 0v6h14z"/><path d="M31 50h12M33 54h8"/><path d="M37 22v-6M22 28l-4-3M52 28l4-3"/>
      <circle cx="62" cy="22" r="6"/><path d="M62 12v4M62 28v4M52 22h4M68 22h4"/>
      <path d="M12 66l10-8h14l10 4H34M12 78l8-4h20l24-14c4-2 7 2 4 5L46 80H18"/>
    </svg></div><div class="label">Custom Solutions</div></div>

  <div class="card" style="left:367px"><div class="icon">
    <svg class="line-ico" width="90" height="90" viewBox="0 0 90 90" aria-hidden="true">
      <circle cx="47" cy="26" r="14"/><path d="M40 26l5 5 9-9"/><path d="M38 38l-4 14 7-4 6 6 2-14M56 38l3 14-7-4"/>
      <path d="M12 66l10-8h14l10 4H34M12 78l8-4h20l24-14c4-2 7 2 4 5L46 80H18"/>
    </svg></div><div class="label">Quality &amp; Compliance</div></div>

  <div class="card" style="left:634px"><div class="icon">
    <svg class="line-ico" width="90" height="90" viewBox="0 0 90 90" aria-hidden="true">
      <circle cx="52" cy="48" r="24"/><path d="M46 18h12M52 18v6M72 28l4-4"/>
      <path d="M56 34L44 50h10l-4 16 14-20H54z"/><path d="M8 40h16M12 50h12M8 60h16"/>
    </svg></div><div class="label">Fast Turnaround</div></div>

  <div class="card" style="left:893px"><div class="icon">
    <svg class="line-ico" width="90" height="90" viewBox="0 0 90 90" aria-hidden="true">
      <path d="M45 6l3 6 6 1-4 4 1 6-6-3-6 3 1-6-4-4 6-1z"/>
      <circle cx="45" cy="38" r="9"/><path d="M30 76V64a15 15 0 0 1 30 0v12"/>
      <circle cx="22" cy="46" r="7"/><path d="M10 76V68a12 12 0 0 1 18-10"/>
      <circle cx="68" cy="46" r="7"/><path d="M80 76V68a12 12 0 0 0-18-10"/>
    </svg></div><div class="label">Expert Team</div></div>
</section>

<section>
  <div class="abs about-band"></div>
  <div class="abs about-photo" role="img" aria-label="Kraft paper bags, black pouches and bottles on a table"></div>
  <h2 class="abs heading" style="left:624px;top:1258px;font-size:60px">About Us</h2>
  <div class="abs" style="left:626px;top:1330px;width:112px;height:2px;background:var(--blue-line)"></div>
  <div class="abs" style="left:626px;top:1328px;width:6px;height:6px;background:var(--blue);transform:rotate(45deg)"></div>
  <p class="abs about-text">Brivo Packworks is a family-owned business in Fairmont, Ohio, with extensive experience in manufacturing and regulatory compliance. We simplify the manufacturing process with step-by-step guidance and a friendly customer service team. Let's take brand to the next level!</p>
  <div class="btn-outline" style="left:625px;top:1498px;width:120px;height:34px;font-size:13px">Learn More</div>
</section>

<section>
  <h2 class="abs heading" style="left:0;top:1712px;width:1200px;text-align:center;font-size:62px">Services</h2>
  <div class="divider" style="left:492px;top:1785px;width:220px"><i></i></div>

  <div class="svc" style="left:113px"><div class="ring">
    <svg class="blue-ico" width="84" height="84" viewBox="0 0 84 84" aria-hidden="true">
      <rect x="44" y="14" width="14" height="56"/><path d="M44 24h6M44 34h8M44 44h6M44 54h8"/>
      <path d="M28 14v38M22 52h12v18H22z"/><circle cx="16" cy="32" r="7"/><path d="M8 44h16v26H8z"/>
      <path d="M62 50l10-10 4 4-10 10z"/><path d="M60 58h14v12H60z"/>
    </svg></div><p>Packaging Design</p></div>

  <div class="svc" style="left:354px"><div class="ring">
    <svg class="blue-ico" width="84" height="84" viewBox="0 0 84 84" aria-hidden="true">
      <path d="M12 34l30 12 30-12M42 46v30M12 34v28l30 14 30-14V34"/>
      <path d="M12 34L4 24l30-10 8 10M72 34l8-10-30-10-8 10"/>
      <rect x="24" y="14" width="8" height="18"/><rect x="38" y="8" width="8" height="22"/><rect x="52" y="14" width="8" height="18"/>
    </svg></div><p>Co-packing</p></div>

  <div class="svc" style="left:599px"><div class="ring">
    <svg class="blue-ico" width="84" height="84" viewBox="0 0 84 84" aria-hidden="true">
      <rect x="26" y="6" width="32" height="10" rx="2"/><path d="M24 16h36v6H24zM22 22h40v56H22z"/>
      <rect x="28" y="32" width="28" height="32"/><path d="M34 56c2-12 10-16 16-16 0 10-6 16-16 16zM34 56l10-10"/>
    </svg></div><p>Nutritional Supplement<br>Packaging</p></div>

  <div class="svc" style="left:849px"><div class="ring">
    <svg class="blue-ico" width="90" height="84" viewBox="0 0 90 84" aria-hidden="true">
      <path d="M26 28h54v28H26L12 42z"/><circle cx="24" cy="42" r="3"/><path d="M2 42h10"/>
      <rect x="40" y="33" width="30" height="18"/><path d="M46 38h18M46 42h12M46 46h18"/>
    </svg></div><p>Private Labeling</p></div>
</section>

<section>
  <div class="abs testi-band"></div>
  <h2 class="abs heading" style="left:0;top:2188px;width:1164px;text-align:center;font-size:60px">Testimonials</h2>
  <div class="divider" style="left:490px;top:2260px;width:220px"><i></i></div>
  <div class="abs testi-frame"></div>
  <div class="abs testi-card"></div>
  <div class="abs avatar"><span role="img" aria-label="Client portrait"></span><em>Marla Quint</em></div>
  <p class="abs quote-text">”Partnering with Brivo Packworks has been a game-changer for our product line. Their sustainable approach and dedication to excellence are truly impressive.”</p>
  <div class="abs stars">★★★★★</div>
  <div class="abs qmark" style="left:384px;top:2313px">“</div>
  <div class="abs qmark" style="left:759px;top:2743px">”</div>
  <div class="abs arrow" style="left:130px;top:2527px"><svg width="14" height="14" viewBox="0 0 14 14"><path d="M9 2 4 7l5 5" fill="none" stroke="#1e90f5" stroke-width="2"/></svg></div>
  <div class="abs arrow" style="left:1042px;top:2527px"><svg width="14" height="14" viewBox="0 0 14 14"><path d="M5 2l5 5-5 5" fill="none" stroke="#1e90f5" stroke-width="2"/></svg></div>
</section>

<section>
  <div class="abs cta-band" role="img" aria-label="Soft background of wrapped parcels tied with twine and green leaves"></div>
  <h2 class="abs cta-title">Superior Quality Packaging<br>Material Manufacturer</h2>
  <div class="abs cta-btn">Get a Free Consultation</div>
</section>

<section>
  <div class="abs contact-band"></div>
  <div class="abs contact-photo" role="img" aria-label="Kraft paper gift box on a sunlit window sill with flowers"></div>
  <h2 class="abs heading" style="left:534px;top:3392px;font-size:60px">Contact Us</h2>
  <div class="abs" style="left:546px;top:3476px;width:110px;height:2px;background:var(--blue-line)"></div>
  <div class="abs" style="left:544px;top:3474px;width:6px;height:6px;background:var(--blue);transform:rotate(45deg)"></div>
  <p class="abs" style="left:547px;top:3502px;font-size:13.5px;color:#333">For more information,Please fill out the following and we will be in touch shortly</p>
  <div class="field" style="left:540px;top:3550px;width:268px">First Name</div>
  <div class="field" style="left:835px;top:3550px;width:268px">Last Name</div>
  <div class="field" style="left:540px;top:3623px;width:268px">Phone</div>
  <div class="field" style="left:835px;top:3623px;width:268px">Company Name</div>
  <div class="field" style="left:540px;top:3694px;width:563px;height:44px;padding-top:15px">Email</div>
  <div class="abs send">Send</div>
</section>

<footer>
  <div class="abs footer"></div>
  <div class="abs brand" style="left:98px;top:4016px;font-size:21px"><b></b>Brivo Packworks</div>
  <div class="social" style="left:115px"></div>
  <div class="social" style="left:164px"></div>
  <div class="social" style="left:211px"></div>

  <h3 class="foot-h" style="left:337px">LINKS</h3>
  <ul class="abs foot-links">
    <li>About Us</li><li>Services</li><li>Case Studies</li><li>FAQ</li><li>Contact Us</li>
  </ul>

  <h3 class="foot-h" style="left:543px">CONTACT US</h3>
  <div class="info-ico" style="top:4004px"><svg width="18" height="18" viewBox="0 0 18 18"><path d="M9 1a6 6 0 0 0-6 6c0 4.5 6 10 6 10s6-5.5 6-10a6 6 0 0 0-6-6zm0 8.5A2.5 2.5 0 1 1 9 4.5a2.5 2.5 0 0 1 0 5z" fill="#25243f"/></svg></div>
  <p class="info" style="top:3996px;left:603px">ADDRESS:<br>&nbsp;465,Lorem ipsum<br>&nbsp; been the</p>
  <div class="info-ico" style="top:4078px"><svg width="18" height="18" viewBox="0 0 18 18"><path d="M4 1.5l3 3-1.8 2.2a10 10 0 0 0 6 6L13.5 11l3 3-2 2.5C8 16 2 10 1.5 3.5z" fill="#25243f"/></svg></div>
  <p class="info" style="top:4072px">PHONE:<br>+1 888 888 8888</p>
  <div class="info-ico" style="top:4155px"><svg width="18" height="14" viewBox="0 0 18 14"><rect x="1" y="1" width="16" height="12" rx="1.5" fill="#25243f"/><path d="M1.5 2 9 8l7.5-6" fill="none" stroke="#fff" stroke-width="1.5"/></svg></div>
  <p class="info" style="top:4150px;font-size:15px">EMAIL:<br>info@brivopackworks.example</p>

  <h3 class="foot-h" style="left:818px">NEWSLETTER SIGN UP</h3>
  <p class="abs" style="left:822px;top:3996px;width:300px;font-size:15px;line-height:26px;color:var(--white)">To stay up to date on all the letest news&nbsp; from us</p>
  <div class="abs news-field">Email</div>
  <div class="abs subscribe">Subscribe</div>

  <div class="abs rule"></div>
  <p class="abs copyright">© 2024 Company Name, Inc. All Rights Reserved.</p>
</footer>

</body>
</html>
```